Some good designs here, but modifications required:
1) in the UK, we refer to cell phones as mobile phones, so the number should be written with an 'M' rather than a 'C' before it, or 'Mobile' rather than 'Cell'.
2) ensure that the compliment slip includes the business address and contact details, with the email address: info@brightarc-mail.com.
3) I prefer the 'with compliments' to go in the bottom right hand corner, thereby leaving space for a note on the compliment slip.
I have just had a new logo designed, but have not yet received it to upload. Please see Vela Grin Logo competition (now closed) where draft 79 was the winner.
Business cards
A4 letterhead sheets
Compliment slips (one third of an A4 sheet)

```html
<!DOCTYPE html>
<html lang="en">
<head>
<meta charset="utf-8">
<title>Velagrin stationery set</title>
<link rel="stylesheet" href="https://fonts.googleapis.com/css2?family=Open+Sans:wght@400;700&family=Dancing+Script:wght@500&display=swap">
<style>
:root{
  --magenta:#a8195a;
  --magenta-deep:#7f0c40;
  --magenta-soft:#b9386f;
  --band-grey:#c9cacc;
  --band-grey-dark:#b5b6b8;
  --ink:#4a4a4a;
  --ink-light:#ffffff;
  --paper:#ffffff;
  --guide:#c4c4c4;
}
*{margin:0;padding:0;box-sizing:border-box}
html,body{width:1200px;height:799px;overflow:hidden;background:var(--paper)}
body{position:relative;font-family:"Open Sans",Arial,sans-serif;color:var(--ink)}
.guide{position:absolute;left:0;width:276px;border-top:2px dashed var(--guide)}
.sheet{position:absolute;background:var(--paper);box-shadow:0 2px 6px rgba(0,0,0,.22);overflow:hidden}
.band{position:absolute;left:0;right:0;top:0;background:var(--band-grey)}
.column{position:absolute;left:0;background:var(--magenta-soft)}
.corner{position:absolute;left:0;top:0;background:var(--magenta-deep)}
.brand{position:absolute;display:flex;align-items:center;gap:6px;font-weight:700;color:var(--magenta);letter-spacing:-.5px;line-height:1}
.brand .dot{border-radius:50%;background:var(--magenta)}
.services{position:absolute;display:grid;grid-template-columns:auto auto;column-gap:14px;color:var(--ink-light);font-size:5px;line-height:7px}
.services li{list-style:none}
.small{position:absolute;font-size:5px;line-height:7px;color:var(--ink)}
.compliments{position:absolute;font-family:"Dancing Script",cursive;color:var(--magenta);font-size:30px}
</style>
</head>
<body>

<div class="guide" style="top:240px"></div>
<div class="guide" style="top:468px"></div>

<!-- Letterhead -->
<section class="sheet letterhead" style="left:276px;top:19px;width:408px;height:749px">
  <div class="band" style="height:58px"></div>
  <div class="column" style="top:58px;width:48px;height:570px"></div>
  <div class="corner" style="width:48px;height:58px"></div>
  <div class="brand" style="left:60px;top:20px;font-size:20px"><span class="dot" style="width:12px;height:12px"></span>Velagrin</div>
  <ul class="services" style="left:262px;top:12px">
    <li>Smile Makeovers</li><li>Invisible Braces</li>
    <li>Teeth Whitening</li><li>Crowns &amp; Bridges</li>
    <li>Dental Implants</li><li>Hygiene Visits</li>
    <li>Veneers</li><li>Family Care</li>
  </ul>
  <p class="small" style="left:70px;top:652px">Vela Grin Ltd<br>14 Harbour Lane, Kingsbridge, Devon TQ7 1AB<br>T 01548 000 112 &nbsp; M 07700 900 245<br>info@brightarc-mail.com &nbsp; www.velagrin-dental.example</p>
</section>

<!-- Compliment slip -->
<section class="sheet slip" style="left:492px;top:168px;width:660px;height:300px">
  <div class="band" style="height:84px"></div>
  <div class="column" style="top:84px;width:72px;height:216px"></div>
  <div class="corner" style="width:72px;height:84px"></div>
  <div class="brand" style="left:86px;top:30px;font-size:26px"><span class="dot" style="width:15px;height:15px"></span>Velagrin</div>
  <ul class="services" style="left:468px;top:18px;font-size:6px;line-height:9px">
    <li>Smile Makeovers</li><li>Invisible Braces</li>
    <li>Teeth Whitening</li><li>Crowns &amp; Bridges</li>
    <li>Dental Implants</li><li>Hygiene Visits</li>
    <li>Veneers</li><li>Family Care</li>
  </ul>
  <p class="small" style="left:182px;top:124px;font-size:6px;line-height:8px">Vela Grin Ltd<br>14 Harbour Lane, Kingsbridge, Devon TQ7 1AB<br>T 01548 000 112 &nbsp; M 07700 900 245<br>info@brightarc-mail.com</p>
  <p class="compliments" style="left:430px;top:188px">with compliments</p>
</section>

<!-- Business card, front -->
<section class="sheet card-front" style="left:233px;top:343px;width:247px;height:149px;background:var(--magenta)">
  <div class="band" style="height:48px;left:auto;width:190px;right:0"></div>
  <div class="corner" style="width:57px;height:48px"></div>
  <div class="brand" style="left:64px;top:14px;font-size:19px"><span class="dot" style="width:11px;height:11px"></span>Velagrin</div>
  <ul class="services" style="left:16px;top:62px;font-size:6px;line-height:9px">
    <li>Smile Makeovers</li><li>Invisible Braces</li>
    <li>Teeth Whitening</li><li>Crowns &amp; Bridges</li>
    <li>Dental Implants</li><li>Hygiene Visits</li>
    <li>Veneers</li><li>Family Care</li>
  </ul>
</section>

<!-- Business card, back -->
<section class="sheet card-back" style="left:336px;top:420px;width:240px;height:144px">
  <div class="column" style="top:0;width:34px;height:144px"></div>
  <div class="corner" style="width:34px;height:30px"></div>
  <div class="brand" style="left:42px;top:22px;font-size:14px"><span class="dot" style="width:8px;height:8px"></span>Velagrin</div>
  <p class="small" style="left:148px;top:20px">Dr Elena Marsh<br>Principal Dentist<br>BDS MFDS</p>
  <p class="small" style="left:84px;top:80px">Vela Grin Ltd<br>14 Harbour Lane<br>Kingsbridge TQ7 1AB</p>
  <p class="small" style="left:150px;top:80px">T 01548 000 112<br>M 07700 900 245<br>info@brightarc-mail.com</p>
</section>

<!-- Envelope -->
<section class="envelope" style="position:absolute;left:708px;top:504px;width:444px;height:276px">
  <svg width="444" height="276" viewBox="0 0 444 276" style="position:absolute;left:0;top:0" aria-hidden="true">
    <rect x="0" y="40" width="444" height="236" fill="var(--paper)" style="filter:drop-shadow(0 2px 3px rgba(0,0,0,.22))"/>
    <polygon points="0,40 222,0 444,40 444,86 0,86" fill="var(--band-grey)"/>
    <rect x="0" y="86" width="58" height="190" fill="var(--magenta-soft)"/>
    <rect x="58" y="40" width="22" height="46" fill="var(--magenta-deep)"/>
  </svg>
  <p class="small" style="left:170px;top:20px">Vela Grin Ltd, 14 Harbour Lane, Kingsbridge TQ7 1AB<br>T 01548 000 112 &nbsp; info@brightarc-mail.com</p>
  <div class="brand" style="left:90px;top:50px;font-size:26px"><span class="dot" style="width:15px;height:15px"></span>Velagrin</div>
</section>

</body>
</html>
```